Torvane Staffing - Mission Poster Design

We are a staffing and recruiting firm with multiple locations across the US. I am seeking a clean modern design highlighting our Mission Statement: Torvane Staffing...Linking Bright Talent with Bold Employers! This design will be framed and placed at the entrance of all of our offices. My website is www.torvanestaffing.example

Target Market(s)

Will be our company mission with a poster prominently placed in each office.

Industry/Entity Type

Staffing

Requirements
Must have
• Must be professional, clean and eye catching. We want to embrace diversity, so we like a variety of people if people will be a focal part.

```html
<!DOCTYPE html>
<html lang="en">
<head>
<meta charset="utf-8">
<title>Torvane Staffing – Mission Poster</title>
<link href="https://fonts.googleapis.com/css2?family=Bebas+Neue&family=Oswald:wght@300&family=Open+Sans:wght@400;600&display=swap" rel="stylesheet">
<style>
  :root {
    --red: #e0413a;
    --yellow: #e3c22a;
    --green: #2b7f45;
    --indigo: #3f3779;
    --paper: #ffffff;
    --frame: #5f6a63;
    --backdrop: #e9e9e6;
    --ink: #222222;
  }
  * { margin: 0; padding: 0; box-sizing: border-box; }
  html, body { width: 1200px; height: 960px; overflow: hidden; }
  body {
    background: var(--backdrop);
    display: flex;
    align-items: center;
    justify-content: center;
  }
  .poster {
    position: relative;
    width: 500px;
    height: 900px;
    background: var(--paper);
    border: 10px solid var(--frame);
    display: flex;
    flex-direction: column;
    align-items: center;
    overflow: hidden;
  }
  .color-band {
    display: flex;
    width: 100%;
    height: 16px;
  }
  .color-band span { flex: 1; }
  .color-band .red { background: var(--red); }
  .color-band .yellow { background: var(--yellow); }
  .color-band .green { background: var(--green); }
  .color-band .indigo { background: var(--indigo); }

  .brand {
    margin-top: 62px;
    display: flex;
    align-items: center;
    gap: 10px;
    font-family: "Open Sans", sans-serif;
    font-weight: 600;
    font-size: 34px;
    color: var(--indigo);
  }
  .brand-dot {
    width: 16px; height: 16px;
    border-radius: 50%;
    background: var(--red);
  }

  .mission {
    margin-top: 36px;
    text-align: center;
    font-family: "Bebas Neue", sans-serif;
    line-height: 0.95;
  }
  .mission .line { display: block; }
  .line-1 { font-size: 118px; color: var(--green); }
  .line-2 { font-size: 92px; }
  .line-3 {
    font-family: "Oswald", sans-serif;
    font-weight: 300;
    font-size: 40px;
    color: var(--green);
    line-height: 1.2;
  }
  .line-4 { font-size: 60px; }
  .yellow-text { color: var(--yellow); }
  .indigo-text { color: var(--indigo); }
  .red-text { color: var(--red); }

  .website {
    position: relative;
    margin-top: 30px;
    padding: 5px 12px;
    border: 1px solid #9a9a9a;
    font-family: "Open Sans", sans-serif;
    font-size: 19px;
    color: var(--ink);
    transform: rotate(-1deg);
  }
  .website::before, .website::after {
    content: "";
    position: absolute;
    width: 5px; height: 5px;
    background: var(--red);
  }
  .website::before { top: -3px; left: -3px; }
  .website::after { bottom: -3px; right: -3px; }

  .team-photo {
    position: absolute;
    left: 0; right: 0; bottom: 0;
    height: 270px;
    background: linear-gradient(180deg, #f2f2f2 0%, #d9d4cf 35%, #6b6a72 100%);
  }
</style>
</head>
<body>
  <main class="poster">
    <div class="color-band">
      <span class="red"></span><span class="yellow"></span><span class="green"></span><span class="indigo"></span>
    </div>

    <div class="brand">
      <span class="brand-dot"></span>
      <span class="brand-name">Torvane Staffing</span>
    </div>

    <h1 class="mission">
      <span class="line line-1">Linking</span>
      <span class="line line-2"><span class="yellow-text">Bright</span> <span class="indigo-text">Talent</span></span>
      <span class="line line-3">WITH</span>
      <span class="line line-4"><span class="indigo-text">Bold</span> <span class="red-text">Employers!</span></span>
    </h1>

    <p class="website">www.torvanestaffing.example</p>

    <div class="team-photo" role="img" aria-label="Photo of a diverse group of five smiling professionals holding large colourful jigsaw puzzle pieces"></div>
  </main>
</body>
</html>
```